依頼詳細
弊社で取り扱う禁煙補助薬「ベルナミンパッチ」及び「ベルナミンガム」に関してA3のポスター及びA4チラシ(両面)をお願いいたします。
ポスター・チラシのイメージはポジティブなイメージにして欲しいです。
ポスターは特に禁煙メリットと方法がよく分かるインパクトが欲しいです。
チラシは表面は禁煙メリットと禁煙の方法としてのベルナミンがよく分かるようにして欲しいです。
裏面は、禁煙のコラムを文字中心で載せたいと思います。
全体を通してお願いしたいのは、危機感を絶対にあおらないイメージにしてください。
記載項目
ポスター:キャッチフレーズとして以下の3点と製品情報を入れてください。
「『禁煙』しないでタバコをやめる」・「禁煙支援薬剤師に相談」・「当店でベルナミン購入の方は「禁煙日記」と「すっきり道場」(24時間メール禁煙サポート:通常参加費10000円)が無料」(語尾などアレンジ可)
(ここで言う『禁煙』は辛い・苦しい・イライラ・我慢など、禁煙のネガティブなイメージをさしています)
製品情報:ベルナミンパッチstep1 14枚入り 5400円・1枚バラ売り 400円
ベルナミンパッチstep2 14枚入り 4800円・1枚バラ売り 380円
ベルナミン(ミント・フルーツ) 30個入り 2600円・1個バラ売り 100円

チラシ表面:上記に加え、禁煙してよかったこと。
(仕事や勉強に集中できるようになった・家族から信頼されるようになった・風邪を引きづらくなった・咳や痰が少なくなった・脱毛が減った・自らのタバコのにおいを気にしなくて良くなった・シミやしわが減り肌のつや・ハリが良くなった)

チラシ裏面:禁煙コラム(後述)
サイズ
ポスターはA3・チラシはA4両面
ページ数
両面
希望イメージ
シンプル 複雑
単色 カラフル
暗い 明るい
日常 高級
遊び心 厳粛
未来的 伝統的
女性的 男性的
希望する色
特にはないですが、とにかく明るい感じでお願いしたいです。
納品ファイル
• 高解像度JPG (.jpg)
• イラストレーター形式 (.ai)
補足説明
禁煙コラム1は以下の内容です。

タバコをやめると、こんな良い変化が・・・

1分禁煙すると・・・タバコのダメージから回復しようとする機能が働き始める。

20分で・・・血圧は正常近くまで下降する。脈拍も正常付近に復帰する。手の体温が聖女まで上昇する。

8時間で・・・血中の一酸化炭素レベルが正常域に戻り、血中酸素分圧が正常になって運動能力が改善する。

24時間で・・・心臓発作の確率が下がる。

48時間で・・・臭いと味の感覚が復活し始める。

48~72時間で・・・ニコチンが体から完全に抜ける。

72時間で・・・気管支の収縮がとれ、呼吸が楽になる。肺活量が増加し始める。

2週~3週間で・・・体の循環が改善する。歩行が楽になる。肺活量は30%回復する。

1~9ヶ月で・・・咳・静脈うっ血・全身倦怠・全身倦怠・呼吸促吐拍が改善する。

5年で・・・肺がんになる確率が半分に減る。

10年で・・・前がん状態の細胞が修復される。口腔がん・咽頭がん・食道がん・膀胱がん・胃がん・腎がん・すい臓がんになる確立が減少する。

しかし、上記のすべての利点は、たった一本のタバコで失われてしまう。
ベルナミンの製品ページはこちらです。
参考にしていただければ助かります。

http://www.velnamin.jp/patch/pa_products.html
禁煙コラム2つ目です。

禁煙に役立つ日常生活の工夫

吸いたくなったときには、次の方法から選んで試してみて、自分にあったやり方を見つけましょう。

・冷たい水や熱いお茶を飲む(ポイントは温度刺激と頻度。唇がしびれるほどの刺激が効果的)

・痛みや刺激で気を紛らわす(ボールペンなど、とがったものを利用して手のひらを押す。耳たぶを爪の先で押さえるのも有効。)

・歯ブラシを利用する(くわえる・噛む・軽く動かすなど・・・。食後すぐ、歯磨きで口をさっぱりさせるのも効果的。)

・宴会や煙の多い場所を避ける(禁煙をスタートした2週間は「逃げるが勝ち!」やむを得ず出席する場合は、吸う人の隣は絶対避けて、ノンアルコールの飲み物を用意しておこう。)

・野菜を食べる(イライラを抑え、便通を整える。細くきった料理用昆布は、口寂しさの解消にも。)

・絶えず体を動かす。深呼吸する(吸いたくなったら、とにかく動くこと。散歩・体操・入浴・掃除・歩く・ゆするでもOK!)

・その他・・・音楽・趣味に没頭する、マスクをする。寝る。コーヒーで吸いたくなる人は紅茶や日本茶に変える。あったかいミルクを飲む。禁煙日記をつける等
禁煙コラム1の「手の体温が聖女まで上昇する」→「手の体温が正常まで上昇する」にしてください。

以下は禁煙コラム3です。

mg数の少ないタバコのほうが害が多い?

→タバコをやめるためにまずmg数を落とそうと考えていませんか?
実は、mg数が少ないほうが体に有害ということをご存知でしょうか。
mg数の少ないタバコはニコチンの量こそ少ないですが、有害物質は同じだけ含まれています。
また、mg数の少ないタバコをすうときは、ニコチンの不足分を補おうと、深く吸い込んでしまう傾向にあります。
その為、有害物質が肺の奥まで行き渡ってしまうためタバコの害が大きいのです。
タバコのmg数で心筋梗塞などの発生率をみると、mg数の少ないタバコを吸っている人のほうが、mg数の多いタバコを吸っている人より高いというデータもあります。

電子タバコにも害がある?

→電子タバコの中には、ニコチンが少量含まれているものがあり、それがやめられなくなる人もいます。
また、水蒸気だけが常温で煙のように立ち上るということはありえません。
ということは、水蒸気以外のものも含まれているはずです。
含まれているものが有害かどうかは分かりませんが、いずれにせよ避けた方がよさそうです。

未成年(小・中・高校生)のほうがニコチン依存が強い?

→実は、未成年のほうが短い期間でニコチン依存ができてしまいます。
たった一本吸ってしまっただけでニコチン依存ができ、タバコがやめられなくなってしまう方も居ます。
ただ、未成年のニコチン依存は、お薬を使うと成人より少ない期間(早い人はパッチ1~3枚程度)で克服できる可能性があります。
お早めにご相談下さい。

タバコをやめると太る?
→禁煙した人のうち2/3の人に、食事量が増えなくても2kg程度の体重増加が認められます。
禁煙により胃腸への血流が回復して、消化吸収が改善されることからです。
また、タバコで麻痺していた味覚が回復して、食べ物が美味しく感じられることや、口寂しさから食事量が増えることもあります。
これは、体が正常に戻った証拠の2kgともいえます。
ただ、ニコチン切れのイライラから食事量が増え、2kg以上の体重増加するケースもあります。
これには、お薬を使うことでイライラを抑え、食事量を過度に増やさないようにしてくれますのでオススメです。
もう少し、いろいろな提案を見たいと思いましたので、締め切りを延ばしたいと思います。

弊社のポスターイメージは、morat様のご提案が近いです。
こういった分かりやすくて見やすい、そして色味の明るいものを希望しています。
http://www.quorvix.jp/work/proposal/2847315

チラシのイメージはtokunaga様のご提案が近いです。
禁煙のメリットが伝わりやすいと思います。
また、裏のコラムもきれいにまとまっていて分かりやすいと思いました。
http://www.quorvix.jp/work/proposal/2849022

多数のご提案、お待ちしておりますので、宜しくお願いいたします。

今回選んだ理由と致しましては、ポスターのインパクト、メッセージ性、チラシのまとめ方などを総合的に鑑みて、tokunaga様の作品が一番弊社のイメージに合うと思ったからです。
特に今回のコンセプト、「危機感をあおらない」ということを理解していただいて、誠実に作られたのだなということが一番伝わってきた作品でした。
以上の理由により、tokunaga様の作品を選ばせていただきました。

弊社のポスター・チラシ作成コンペに提案いただきました皆様、本当にありがとうございます。
素晴らしい提案が多く、選考に非常に迷いました。
このように沢山いろいろな感性を持った方々に、作品を提案いただけたのはうれしい限りです。
今回は残念ながらひとつの提案のみを採用させていただく形になりましたが、また、このような機会がありましたら、ご提案いただけたらと思います。
今回は、本当にありがとうございました。

```html
<!DOCTYPE html>
<html lang="ja">
<head>
<meta charset="utf-8">
<link href="https://fonts.googleapis.com/css2?family=Noto+Sans+JP:wght@400;700;900&display=swap" rel="stylesheet">
<style>
:root{
  --ink:#111;
  --paper:#fff;
  --accent:#d7141b;
  --muted:#cfcfcf;
}
*{margin:0;padding:0;box-sizing:border-box}
html,body{width:851px;height:1200px;overflow:hidden;background:var(--paper)}
body{font-family:"Noto Sans JP",sans-serif;color:var(--paper)}
.sheet{position:relative;width:851px;height:1200px}
.dark{position:absolute;left:0;top:0;width:851px;height:845px;background:var(--ink)}
.side-title{position:absolute;left:12px;top:12px;width:40px;height:500px;background:var(--accent);
  writing-mode:vertical-rl;font-weight:900;font-size:23px;line-height:40px;padding-top:14px;letter-spacing:1px}
.side-note{position:absolute;right:10px;top:12px;width:36px;height:500px;background:var(--paper);color:var(--ink);
  writing-mode:vertical-rl;font-weight:700;font-size:14px;line-height:36px;padding-top:8px;letter-spacing:0}
.timeline{position:absolute;left:64px;top:34px;width:730px;list-style:none}
.timeline li{display:flex;align-items:flex-start;min-height:37px;margin-bottom:4px;font-size:12.5px;line-height:17px;font-weight:700}
.badge{flex:0 0 auto;width:30px;height:30px;border-radius:50%;background:var(--paper);color:var(--ink);
  display:flex;align-items:center;justify-content:center;font-size:11px;font-weight:900;margin-right:10px;white-space:nowrap}
.badge.wide{width:auto;min-width:42px;padding:0 7px;border-radius:15px;font-size:10px}
.badge small{font-size:7px}
.timeline p{padding-top:6px}
.tips-head{position:absolute;left:12px;top:520px;width:827px;height:28px;background:var(--paper);color:var(--ink);
  font-weight:900;font-size:17px;line-height:28px;padding-left:14px}
.tips-intro{position:absolute;left:24px;top:556px;font-size:10.5px}
.tips{position:absolute;left:24px;top:578px;width:810px;list-style:none}
.tips li{font-size:13.5px;font-weight:900;line-height:17px;margin-bottom:15.5px}
.tips li span{font-size:9px;font-weight:700;color:var(--paper);background:var(--accent);padding:1px 4px;margin-left:4px}
.qa{position:absolute;left:12px;top:858px;width:827px;display:grid;grid-template-columns:repeat(4,1fr);gap:12px;color:var(--ink)}
.qa article{border-top:2px solid var(--ink);padding-top:6px}
.qa h3{display:flex;font-size:12px;line-height:16px;font-weight:900;min-height:36px}
.qa h3 b,.qa .a{color:var(--accent);font-size:22px;line-height:22px;margin-right:5px;font-weight:900}
.qa .body{display:flex;margin-top:6px}
.qa p{font-size:9.3px;line-height:14.5px;text-align:justify}
.nosmoke{display:block;margin:10px 0 0 auto}
</style>
</head>
<body>
<main class="sheet">
  <section class="dark">
    <h2 class="side-title">タバコをやめると、こんな良い変化が・・・</h2>
    <p class="side-note">しかし、上記のすべての利点は、たった一本のタバコで失われてしまう。</p>
    <ol class="timeline">
      <li><span class="badge">1<small>分</small></span><p>禁煙すると、タバコのダメージから回復しようとする機能が働き始める。</p></li>
      <li><span class="badge">20<small>分</small></span><p>で血圧は正常近くまで下降する。脈拍も正常付近に復帰する。手の体温が正常まで上昇する。</p></li>
      <li><span class="badge">8<small>時間</small></span><p>で血中の一酸化炭素レベルが正常域に戻り、血中酸素分圧が正常になって運動能力が改善する。</p></li>
      <li><span class="badge">24<small>時</small></span><p>間で心臓発作の確率が下がる。</p></li>
      <li><span class="badge">48<small>時</small></span><p>間で臭いと味の感覚が復活し始める。</p></li>
      <li><span class="badge wide">48~72</span><p>時間でニコチンが体から完全に抜ける。</p></li>
      <li><span class="badge">72<small>時</small></span><p>間で気管支の収縮がとれ、呼吸が楽になる。肺活量が増加し始める。</p></li>
      <li><span class="badge wide">2週~3週</span><p>間で体の循環が改善する。歩行が楽になる。肺活量は30%回復する。</p></li>
      <li><span class="badge wide">1~9<small>ヶ月</small></span><p>で咳・静脈うっ血・全身倦怠・呼吸促迫が改善する。</p></li>
      <li><span class="badge">5<small>年</small></span><p>で肺がんになる確率が半分に減る。</p></li>
      <li><span class="badge">10<small>年</small></span><p>で前がん状態の細胞が修復される。<br>口腔がん・咽頭がん・食道がん・膀胱がん・胃がん・腎がん・すい臓がんになる確率が減少する。</p></li>
    </ol>
    <h2 class="tips-head">禁煙に役立つ日常生活の工夫</h2>
    <p class="tips-intro">吸いたくなったときには、次の方法から選んで試してみて、自分にあったやり方を見つけましょう。</p>
    <ul class="tips">
      <li>・冷たい水や熱いお茶を飲む<span>ポイントは温度刺激と頻度。唇がしびれるほどの刺激が効果的</span></li>
      <li>・痛みや刺激で気を紛らわす<span>ボールペンなどで手のひらを押す。耳たぶを爪の先で押さえるのも有効</span></li>
      <li>・歯ブラシを利用する<span>くわえる・噛む・軽く動かすなど。食後すぐの歯磨きも効果的</span></li>
      <li>・宴会や煙の多い場所を避ける<span>最初の2週間は「逃げるが勝ち!」吸う人の隣は避けよう</span></li>
      <li>・野菜を食べる<span>イライラを抑え、便通を整える。細く切った昆布は口寂しさの解消にも</span></li>
      <li>・絶えず体を動かす。深呼吸する<span>散歩・体操・入浴・掃除・歩く・ゆするでもOK!</span></li>
      <li>・その他…音楽・趣味に没頭する／マスクをする／寝る／コーヒーで吸いたくなる人は紅茶や日本茶に変える／<br>&nbsp;&nbsp;あったかいミルクを飲む／禁煙日記をつける等</li>
    </ul>
  </section>

  <section class="qa">
    <article>
      <h3><b>Q</b>mg数の少ないタバコのほうが害が多い？</h3>
      <div class="body"><span class="a">A</span><p>タバコをやめるためにまずmg数を落とそうと考えていませんか？実は、mg数が少ないほうが体に有害ということをご存知でしょうか。mg数の少ないタバコはニコチンの量こそ少ないですが、有害物質は同じだけ含まれています。また、ニコチンの不足分を補おうと、深く吸い込んでしまう傾向にあります。その為、有害物質が肺の奥まで行き渡ってしまうのです。心筋梗塞などの発生率は、mg数の少ないタバコを吸っている人のほうが高いというデータもあります。</p></div>
    </article>
    <article>
      <h3><b>Q</b>電子タバコにも害がある？</h3>
      <div class="body"><span class="a">A</span><p>電子タバコの中には、ニコチンが少量含まれているものがあり、それがやめられなくなる人もいます。また、水蒸気だけが常温で煙のように立ち上るということはありえません。ということは、水蒸気以外のものも含まれているはずです。含まれているものが有害かどうかは分かりませんが、いずれにせよ避けた方がよさそうです。</p></div>
    </article>
    <article>
      <h3><b>Q</b>タバコをやめると太る？</h3>
      <div class="body"><span class="a">A</span><p>禁煙した人の2/3に、食事量が増えなくても2kg程度の体重増加が認められます。胃腸への血流が回復して、消化吸収が改善されるからです。また、味覚が回復して食べ物が美味しく感じられることもあります。これは体が正常に戻った証拠の2kgともいえます。ただ、イライラから食事量が増えるケースもあり、お薬でイライラを抑えるのがオススメです。</p></div>
    </article>
    <article>
      <h3><b>Q</b>未成年（小・中・高校生）のほうがニコチン依存が強い？</h3>
      <div class="body"><span class="a">A</span><p>実は、未成年のほうが短い期間でニコチン依存ができてしまいます。たった一本吸っただけで依存ができる方も居ます。ただ、お薬を使うと成人より少ない期間（早い人はパッチ1~3枚程度）で克服できる可能性があります。お早めにご相談下さい。</p></div>
      <svg class="nosmoke" width="70" height="70" viewBox="0 0 70 70" aria-hidden="true">
        <rect x="12" y="31" width="40" height="8" fill="#111"/>
        <rect x="52" y="31" width="6" height="8" fill="#d7141b"/>
        <circle cx="35" cy="35" r="30" fill="none" stroke="#d7141b" stroke-width="6"/>
        <line x1="14" y1="14" x2="56" y2="56" stroke="#d7141b" stroke-width="6"/>
      </svg>
    </article>
  </section>
</main>
</body>
</html>
```